Business card design needed

I have started a new business called Marlow Auto Electrical, although the words Marlow Auto Electrical will be used on signage and documents I actually want to market the business as MAE. The services I offer are Mobile Auto Electrical, Automotive Air Conditioning and Test And Tag. My business will be targetting the Mining Industry, Civil, Rail, Agricultural and Workshop Testing And Tagging. My auto electrical service ranges from fault finding to new vehicle and mine compliance fit outs. I have a very strong focus on quality workmanship. I will upload the logo I have designed and want to use I am happy for the logo colour to change but the design itself must stay the same. I want the design to have a modern, eye catching, energetic feel. As I am a passionate motorsport fan I am happy for this to also influence the design. I am happy for the front of the card to have only the emblem and logo design and the back to have all the info.

Industry/Entity Type

Electrical

Contact Information for Business Card

MAE Marlow Auto Electrical, Dale Penrick, Auto Electrician, Mobile No 0417263859

Requirements
Must have
• On the business card it is mandatory that the following license numbers are shown:

MVRL38462
VDA L071348
ABN 61 839 204 518

```html
<!DOCTYPE html>
<html lang="en">
<head>
<meta charset="utf-8">
<title>Marlow Auto Electrical — Business Card</title>
<link rel="stylesheet" href="https://fonts.googleapis.com/css2?family=Questrial&display=swap">
<style>
  :root {
    --backdrop: #d8d2c8;
    --card: #0b0b0b;
    --ink: #f4f4f4;
    --ink-soft: #cfcfcf;
    --amber: #f6b00f;
    --rule: #6a6a6a;
  }
  * { box-sizing: border-box; margin: 0; padding: 0; }
  html, body {
    width: 1200px;
    height: 900px;
    overflow: hidden;
    background: var(--backdrop);
    font-family: "Questrial", "Century Gothic", sans-serif;
  }
  .sheet {
    position: relative;
    width: 1200px;
    height: 900px;
  }
  .card {
    position: absolute;
    left: 320px;
    width: 560px;
    height: 320px;
    background: var(--card);
    color: var(--ink);
    box-shadow: 0 10px 28px rgba(0,0,0,0.28);
  }
  .card--back { top: 100px; }
  .card--front { top: 480px; }

  /* Back: contact side */
  .card--back .brand {
    position: absolute;
    left: 36px;
    top: 56px;
    color: var(--ink);
  }
  .brand__mark {
    font-size: 76px;
    line-height: 0.9;
    letter-spacing: 4px;
  }
  .brand__name {
    font-size: 15px;
    letter-spacing: 1.2px;
    text-transform: uppercase;
    margin-top: 6px;
  }
  .divider {
    position: absolute;
    left: 270px;
    top: 40px;
    width: 1px;
    height: 170px;
    background: var(--rule);
  }
  .person {
    position: absolute;
    right: 36px;
    top: 96px;
    text-align: right;
  }
  .person__name {
    font-size: 26px;
    letter-spacing: 1.5px;
    text-transform: uppercase;
    text-align: left;
  }
  .person__role {
    font-size: 16px;
    letter-spacing: 1.2px;
    text-transform: uppercase;
    color: var(--ink-soft);
    margin-top: 2px;
  }
  .person__phone {
    font-size: 13px;
    letter-spacing: 1.2px;
    text-transform: uppercase;
    margin-top: 14px;
  }
  .licences {
    position: absolute;
    left: 36px;
    right: 36px;
    bottom: 34px;
    display: flex;
    justify-content: space-between;
    font-size: 11px;
    letter-spacing: 1.2px;
    color: var(--ink-soft);
  }
  .licences__group { display: flex; flex-direction: column; gap: 5px; }

  /* Front: emblem side */
  .card--front .brand {
    position: absolute;
    left: 0;
    right: 0;
    top: 100px;
    text-align: center;
    color: var(--amber);
  }
  .card--front .brand__mark { font-size: 92px; }
  .card--front .brand__name { font-size: 17px; margin-top: 8px; }
</style>
</head>
<body>
  <main class="sheet">
    <section class="card card--back" aria-label="Business card back">
      <div class="brand">
        <div class="brand__mark">MAE</div>
        <div class="brand__name">Marlow Auto Electrical</div>
      </div>
      <div class="divider"></div>
      <div class="person">
        <div class="person__name">Dale Penrick</div>
        <div class="person__role">Auto Electrician</div>
        <div class="person__phone">Mobile: 0417263859</div>
      </div>
      <div class="licences">
        <div class="licences__group">
          <span>ABN 61 839 204 518</span>
          <span>MVRL38462</span>
        </div>
        <div class="licences__group">
          <span>&nbsp;</span>
          <span>VDA L071348</span>
        </div>
      </div>
    </section>

    <section class="card card--front" aria-label="Business card front">
      <div class="brand">
        <div class="brand__mark">MAE</div>
        <div class="brand__name">Marlow Auto Electrical</div>
      </div>
    </section>
  </main>
</body>
</html>
```